Business Card Design Project

i have the logo designed.
I require designs for the managing director and the general manager.
we need space for email, and a mobile number.
any other cool stuff/design you guys just let me see what you got.
The managing director card could be black, minimalist, and the cards for the rest of the company could be using the green logo.
it has to impress. transportation market is fragmented, we want to appear professional and sophisticated.
Md: Tarek bani rahim
General manager: omer rahim
clients: procurement heads of contracting companies
Business

```html
<!DOCTYPE html>
<html lang="en">
<head>
<meta charset="utf-8">
<title>Fleetwise Business Cards</title>
<link href="https://fonts.googleapis.com/css2?family=Roboto:wght@400;700&family=PT+Sans&display=swap" rel="stylesheet">
<style>
  :root {
    --backdrop: #3b2a20;
    --card-white: #ffffff;
    --brand-green: #0f7a3c;
    --deep-green: #117a3e;
    --soft-green: #2a9a4e;
    --muted-grey: #b5b5b5;
    --label-white: #ffffff;
  }
  * { margin: 0; padding: 0; box-sizing: border-box; }
  html, body { width: 1200px; height: 913px; overflow: hidden; }
  body {
    background: var(--backdrop);
    font-family: "Roboto", Arial, sans-serif;
    position: relative;
  }
  .card {
    position: absolute;
    width: 480px;
    height: 274px;
    background: var(--card-white);
    box-shadow: 0 6px 18px rgba(0,0,0,0.45);
  }
  .card--front { left: 90px; top: 120px; }
  .card--back-one { left: 630px; top: 120px; }
  .card--back-two { left: 90px; top: 510px; }
  .card--back-three { left: 630px; top: 510px; background: var(--deep-green); }

  .brand-name {
    position: absolute;
    font-weight: 700;
    color: var(--brand-green);
    letter-spacing: 0.5px;
    display: flex;
    align-items: center;
    gap: 12px;
    white-space: nowrap;
  }
  .brand-mark {
    width: 22px; height: 22px;
    border-radius: 50%;
    background: var(--brand-green);
    display: inline-block;
  }
  .card--front .brand-name { left: 110px; top: 42px; font-size: 40px; }
  .holder-name {
    position: absolute; left: 0; right: 0; top: 138px;
    text-align: center; font-size: 17px; letter-spacing: 1px;
    color: var(--brand-green); text-transform: uppercase;
  }
  .holder-role {
    position: absolute; left: 0; right: 0; top: 164px;
    text-align: center; font-size: 12px; color: var(--brand-green);
  }
  .contact-line {
    position: absolute; left: 0; right: 0; bottom: 34px;
    display: flex; justify-content: center; gap: 18px;
    font-size: 12px; color: var(--brand-green);
  }
  .contact-item { display: flex; align-items: center; gap: 5px; }
  .contact-item svg { width: 11px; height: 11px; fill: var(--brand-green); }

  .card--back-one .brand-name { left: 0; right: 0; top: 110px; justify-content: center; font-size: 44px; }
  .card--back-two .brand-name { left: 0; right: 0; top: 90px; justify-content: center; font-size: 38px; }
  .web-faint {
    position: absolute; left: 0; right: 0; bottom: 40px;
    text-align: center; font-size: 10px; letter-spacing: 5px; color: var(--muted-grey);
  }
  .web-light {
    position: absolute; left: 0; right: 0; top: 40px;
    text-align: center; font-size: 11px; letter-spacing: 5px; color: var(--label-white);
  }
  .card--back-three .brand-name {
    right: 40px; bottom: 40px; font-size: 54px; color: var(--soft-green);
  }
  .card--back-three .brand-mark { background: var(--soft-green); width: 30px; height: 30px; }

  .caption {
    position: absolute;
    font-family: "PT Sans", Arial, sans-serif;
    font-size: 28px;
    color: var(--label-white);
  }
  .caption--one { left: 1010px; top: 72px; }
  .caption--two { left: 90px; top: 800px; }
  .caption--three { left: 1010px; top: 800px; }
</style>
</head>
<body>
  <section class="card card--front">
    <div class="brand-name"><span class="brand-mark"></span>Fleetwise</div>
    <p class="holder-name">Tarek Bani Rahim</p>
    <p class="holder-role">Managing Director</p>
    <div class="contact-line">
      <span class="contact-item">
        <svg viewBox="0 0 10 10" aria-hidden="true"><rect x="2.5" y="0" width="5" height="10" rx="1"/></svg>012.555.0147
      </span>
      <span class="contact-item">
        <svg viewBox="0 0 10 10" aria-hidden="true"><path d="M0 2h10v6H0z M0 2l5 3.5L10 2" /></svg>name@fleetwise.com
      </span>
    </div>
  </section>

  <section class="card card--back-one">
    <div class="brand-name"><span class="brand-mark"></span>Fleetwise</div>
  </section>

  <section class="card card--back-two">
    <div class="brand-name"><span class="brand-mark"></span>Fleetwise</div>
    <p class="web-faint">www.fleetwise.com</p>
  </section>

  <section class="card card--back-three">
    <p class="web-light">www.fleetwise.com</p>
    <div class="brand-name"><span class="brand-mark"></span>Fleetwise</div>
  </section>

  <span class="caption caption--one">Back 1</span>
  <span class="caption caption--two">Back 2</span>
  <span class="caption caption--three">Back 3</span>
</body>
</html>
```